Business Card Design Project

I am community manager and social media strategist. I need a double sided business card with company logo and name. Looking for something professional, elegant but also a little bit original.

Industry/Entity Type

Business

Requirements
Must have
• - The logo and the colours are the company colours and a required to stay.
- The size should be: 84 x 55 mm (or 3.30 x 2.16)
- The file size should be: 1039 x 697 pixels (300 dpi)
- I'd like rounded corners. :)

Use the following contact information for the card:

Lucile Bravant
Stratégie médias sociaux / community management / édition de sites sociaux
mob. : 0687152930
lucile.bravant@maivox.fr
Fil. : @lbravant
Visio : bravant.lucile

```html
<!DOCTYPE html>
<html lang="fr">
<head>
<meta charset="utf-8">
<title>Ventara — carte de visite</title>
<link rel="stylesheet" href="https://fonts.googleapis.com/css2?family=Open+Sans:wght@600&family=Tinos:wght@700&family=Arimo:ital,wght@0,400;1,400&display=swap">
<style>
  :root {
    --backdrop: #b3b3b3;
    --paper: #ffffff;
    --brand-deep: #0a5592;
    --brand: #1670b0;
    --brand-bright: #2a8fd0;
    --brand-pale: #d6e8f5;
    --brand-mist: #eef5fb;
    --ink: #3d3d3d;
    --ink-soft: #6a6a6a;
  }
  * { margin: 0; padding: 0; box-sizing: border-box; }
  html, body {
    width: 1117px; height: 1200px; overflow: hidden;
    background: var(--backdrop);
  }
  .canvas { position: relative; width: 1117px; height: 1200px; }

  .card {
    position: absolute; left: 148px;
    width: 820px; height: 537px;
    border-radius: 30px; overflow: hidden;
  }
  .card--front { top: 40px; background: var(--paper); }
  .card--back {
    top: 620px;
    background: linear-gradient(120deg, var(--brand-deep) 0%, var(--brand) 55%, var(--brand-bright) 100%);
  }

  .card__topband {
    position: absolute; left: 0; top: 0; width: 100%; height: 38px;
    background: linear-gradient(90deg, var(--brand-deep) 0%, var(--brand) 22%, var(--brand-pale) 45%, #ffffff 52%, var(--brand-pale) 60%, var(--brand) 82%, var(--brand-deep) 100%);
  }
  .card__waves, .card__mark-faint, .card__sheen { position: absolute; left: 0; top: 0; width: 100%; height: 100%; }

  .brand {
    position: absolute; left: 38px; top: 70px;
    display: flex; align-items: center; gap: 14px;
  }
  .brand__dot { width: 44px; height: 44px; border-radius: 50%; background: var(--brand); }
  .brand__name {
    font-family: "Open Sans", sans-serif; font-weight: 600;
    font-size: 46px; letter-spacing: 1px; color: var(--brand-deep);
  }

  .person { position: absolute; left: 40px; top: 232px; }
  .person__name {
    font-family: "Tinos", serif; font-weight: 700;
    font-size: 46px; color: var(--ink); line-height: 1;
  }
  .person__role {
    margin-top: 8px;
    font-family: "Arimo", sans-serif; font-style: italic;
    font-size: 17px; color: var(--ink-soft);
  }
  .contact {
    position: absolute; left: 40px; top: 340px; list-style: none;
    font-family: "Arimo", sans-serif; font-size: 23px; line-height: 29px; color: var(--ink);
  }

  .card__backbrand {
    position: absolute; left: 0; top: 0; width: 100%; height: 100%;
    display: flex; flex-direction: column; align-items: center; justify-content: center; gap: 30px;
  }
  .card__backbrand .brand__dot { width: 150px; height: 150px; background: var(--paper); }
  .card__backbrand .brand__name { font-size: 86px; color: var(--paper); letter-spacing: 3px; }
</style>
</head>
<body>
<main class="canvas">

  <section class="card card--front" aria-label="Recto de la carte">
    <svg class="card__mark-faint" viewBox="0 0 820 537" aria-hidden="true">
      <circle cx="640" cy="200" r="150" fill="var(--brand-mist)"/>
    </svg>
    <svg class="card__waves" viewBox="0 0 820 537" preserveAspectRatio="none" aria-hidden="true">
      <defs>
        <linearGradient id="waveDeep" x1="0" x2="1" y1="0" y2="0">
          <stop offset="0" stop-color="#1670b0"/>
          <stop offset="0.5" stop-color="#0a5592"/>
          <stop offset="1" stop-color="#2a8fd0"/>
        </linearGradient>
        <linearGradient id="waveSoft" x1="0" x2="1" y1="0" y2="0">
          <stop offset="0" stop-color="#d6e8f5"/>
          <stop offset="1" stop-color="#5aa6da"/>
        </linearGradient>
      </defs>
      <path d="M0 470 C 260 500, 560 470, 820 360 L820 537 L0 537 Z" fill="url(#waveSoft)" opacity="0.55"/>
      <path d="M0 490 C 300 505, 580 470, 820 400 L820 537 L0 537 Z" fill="#8cc2e6" opacity="0.7"/>
      <path d="M0 505 C 320 515, 600 490, 820 440 L820 537 L0 537 Z" fill="url(#waveDeep)"/>
      <path d="M0 512 C 330 520, 620 500, 820 470" fill="none" stroke="#ffffff" stroke-width="3" opacity="0.7"/>
    </svg>
    <div class="card__topband"></div>

    <div class="brand">
      <span class="brand__dot"></span>
      <span class="brand__name">VENTARA</span>
    </div>

    <div class="person">
      <h1 class="person__name">Lucile Bravant</h1>
      <p class="person__role">Stratégie médias sociaux / community management / édition de sites sociaux</p>
    </div>

    <ul class="contact">
      <li>mob. : 0687152930</li>
      <li>lucile.bravant@maivox.fr</li>
      <li>Fil. : @lbravant</li>
      <li>Visio : bravant.lucile</li>
    </ul>
  </section>

  <section class="card card--back" aria-label="Verso de la carte">
    <svg class="card__sheen" viewBox="0 0 820 537" preserveAspectRatio="none" aria-hidden="true">
      <path d="M0 537 C 250 380, 560 330, 820 120 L820 537 Z" fill="#ffffff" opacity="0.06"/>
      <path d="M0 537 C 300 450, 600 420, 820 260 L820 537 Z" fill="#ffffff" opacity="0.05"/>
    </svg>
    <div class="card__backbrand">
      <span class="brand__dot"></span>
      <span class="brand__name">VENTARA</span>
    </div>
  </section>

</main>
</body>
</html>
```